Property Services Company Needs a Brochure Design

Looking for a new brochure design for an existing property services company.

We provide a range of property services from, market research, real estate brokerage, valuation and appraisal, property development and other real estate consulting services.

We would like a fresh modern brochure design with good graphics and features. Our colours are white, blue and orange.

The design should communicate, attention to detail, superior service delivery and distinction in results.
Updates

I would like the brochure to be roughly about 20 pages.

Containing the following,

1) An introduction
2) Contents Page
2) What we do
3) Our Services
4) Agency & Brokerage
5) Real Estate Consulting
6) Market Research
7) Appraisal & Valuation
8) Project Management
9) Property Development

I would also like icons to represent items 4,5,6,7,8 & 9, they should be represented vertically on each of the pages from the contents page and highlighted individually on the pages that they represent.. i.e. on appraisal & valuation page, all six icons will be arranged vertically and the appraisal and valuations icon will be highlighted.

I will also like to have images that depict the services on the various pages.

I have some pages I think will flow which I will upload shortly.

Industry/Entity Type

Real Estate

Font styles to use
Serif

Colors
f78f20
0455a3

```html
<!DOCTYPE html>
<html lang="en">
<head>
<meta charset="utf-8">
<title>Halvercrest Brochure Spreads</title>
<link rel="stylesheet" href="https://fonts.googleapis.com/css2?family=Open+Sans:wght@400;600;700&display=swap">
<style>
  :root {
    --orange: #f78f20;
    --blue: #0455a3;
    --navy: #0b3a78;
    --ink: #3a3a3a;
    --stage: #2b2b2b;
    --paper: #ffffff;
    --paper-shade: #dcdcdc;
    --band-text: #fde3c4;
  }
  * { margin: 0; padding: 0; box-sizing: border-box; }
  html, body { width: 1200px; height: 900px; overflow: hidden; }
  body { background: var(--stage); font-family: "Open Sans", Arial, sans-serif; position: relative; }

  .spread {
    position: absolute;
    width: 1007px; height: 355px;
    background: radial-gradient(ellipse at 30% 50%, var(--paper) 40%, var(--paper-shade) 100%);
    overflow: hidden;
    box-shadow: 0 6px 14px rgba(0,0,0,.5);
  }
  .spread--intro { left: 113px; top: 88px; }
  .spread--services { left: 111px; top: 503px; }

  .spread__art { position: absolute; inset: 0; width: 1007px; height: 355px; }

  .page-heading {
    position: absolute; font-size: 9.5px; font-weight: 700; color: #111; letter-spacing: .2px;
  }
  .body-copy {
    position: absolute; font-size: 10px; line-height: 11.6px; color: var(--ink);
  }
  .body-copy p + p { margin-top: 11px; }

  .photo {
    position: absolute; left: 505px; top: 112px; width: 317px; height: 243px;
    background: linear-gradient(135deg, #e6e3dc 0%, #c9c2b6 45%, #3a4660 70%, #d9d6d0 100%);
  }

  .contents-list {
    position: absolute; right: 27px; top: 64px; list-style: none; text-align: right;
  }
  .contents-list li {
    height: 28px; font-size: 11.5px; font-weight: 600; color: var(--band-text);
  }

  .service {
    position: absolute; font-size: 16.5px; font-weight: 700;
  }
  .service--blue { color: var(--blue); }
  .service--orange { color: var(--orange); }
  .service-icon { position: absolute; }
</style>
</head>
<body>

<!-- Spread: introduction and contents -->
<section class="spread spread--intro">
  <svg class="spread__art" viewBox="0 0 1007 355" aria-hidden="true">
    <rect x="0" y="0" width="27" height="355" fill="var(--navy)"/>
    <rect x="27" y="0" width="7" height="355" fill="var(--orange)"/>
    <polygon points="287,355 505,150 505,0 542,0 922,355" fill="var(--navy)"/>
    <polygon points="600,54 1007,54 1007,282 844,282" fill="var(--orange)"/>
    <polygon points="287,355 611,50 624,50 300,355" fill="var(--orange)"/>
    <polygon points="542,0 554,0 934,355 922,355" fill="var(--orange)"/>
    <g stroke="#fbe1c2" stroke-width="1">
      <line x1="640" y1="84" x2="1007" y2="84"/>
      <line x1="670" y1="112" x2="1007" y2="112"/>
      <line x1="700" y1="140" x2="1007" y2="140"/>
      <line x1="730" y1="168" x2="1007" y2="168"/>
      <line x1="760" y1="196" x2="1007" y2="196"/>
      <line x1="790" y1="224" x2="1007" y2="224"/>
      <line x1="820" y1="252" x2="1007" y2="252"/>
    </g>
  </svg>

  <h2 class="page-heading" style="left:54px; top:17px;">INTRODUCTION</h2>
  <div class="body-copy" style="left:50px; top:58px; width:425px;">
    <p>HALVERCREST was incorporated in 1984 as an interior design and property development company. Over the years we have expanded our service with a foundation based on core strengths, unrivalled local expertise, network and knowledge combined with strategic partnerships.</p>
    <p>Halvercrest offers a comprehensive range of services on a local, regional, national and international basis to tenants, owners, and investors within the residential and commercial property market.</p>
    <p style="width:390px;">Our clients depend on our ability to draw on years of experience in the local market, our professionals know their communities and the property market inside and out, and provide knowledgeable, creative solutions to all their real estate needs.</p>
    <p style="width:320px;">We currently provide services to corporations, financial institutions, government agencies, public sector entities, developers and investors. Our knowledge, expertise, experience and technological resources allow us to be a superior service provider.</p>
  </div>

  <div class="photo" role="img" aria-label="Photo of a smiling businessman in a suit reading a newspaper on a sofa"></div>

  <h2 class="page-heading" style="right:45px; top:17px;">CONTENT</h2>
  <ul class="contents-list">
    <li>What we do</li>
    <li>Our Services</li>
    <li>Agency &amp; Brokerage</li>
    <li>Real Estate Consulting</li>
    <li>Market Research</li>
    <li>Appraisal &amp; Valuation</li>
    <li>Project Management</li>
    <li>Property Development</li>
  </ul>
</section>

<!-- Spread: what we do and our services -->
<section class="spread spread--services">
  <svg class="spread__art" viewBox="0 0 1007 355" aria-hidden="true">
    <rect x="0" y="0" width="27" height="355" fill="var(--navy)"/>
    <rect x="27" y="0" width="6" height="355" fill="var(--orange)"/>
    <rect x="505" y="319" width="502" height="6" fill="var(--orange)"/>
    <rect x="505" y="325" width="502" height="30" fill="var(--navy)"/>
  </svg>

  <h2 class="page-heading" style="left:54px; top:17px;">WHAT WE DO</h2>
  <div class="body-copy" style="left:50px; top:45px; width:425px;">
    <p>Halvercrest is a leading property services company, incorporated in 1984, providing bespoke solutions in advisory, brokerage and turnkey solutions to owners, occupiers and property investors. Over the years we have expanded our services with a foundation based on core strengths, unrivalled local expertise, network and knowledge combined with strategic partnership. As well as providing property solutions we also develop commercial and residential units.</p>
    <p>Our growth has been based on maintaining relationships with our extensive client base, ranging from financial institutions, government agencies, airlines and servicing companies, manufacturing companies, multinationals and local corporations, to private developers and investors. Our clients depend on our ability to draw on years of experience in the local market, our professionals know their communities and the property market inside and out, and provide knowledgeable, creative solutions to all their real estate needs.</p>
    <p>The combination of our integrated services allows us to provide a superior end to end solution to our clients, customized to their own requirements. Market research is a core component to our business model, allowing us to make informed decisions based based on research findings. Our brokerage team also benefits from this information, allowing our associates to advise clients on how best to maximise return on their investment on the sale or buy side within a short timeline.</p>
    <p>We pay great attention to detail in consideration of our client requirements, delivering mandates with distinction.</p>
  </div>

  <h2 class="page-heading" style="right:22px; top:17px;">OUR SERVICES</h2>

  <!-- Agency & Brokerage -->
  <svg class="service-icon" style="left:520px; top:44px;" width="42" height="52" viewBox="0 0 42 52" aria-hidden="true">
    <rect x="2" y="34" width="7" height="16" fill="var(--orange)"/>
    <rect x="12" y="28" width="7" height="22" fill="var(--orange)"/>
    <rect x="22" y="22" width="7" height="28" fill="var(--orange)"/>
    <rect x="32" y="16" width="7" height="34" fill="var(--orange)"/>
    <polyline points="2,24 12,16 20,20 36,4" fill="none" stroke="var(--orange)" stroke-width="2.5"/>
    <polygon points="30,2 40,1 39,11" fill="var(--orange)"/>
  </svg>
  <div class="service service--blue" style="left:576px; top:68px;">Agency &amp; Brokerage</div>

  <!-- Appraisal & Valuation -->
  <div class="service service--orange" style="right:85px; top:110px;">Appraisal &amp; Valuation</div>
  <svg class="service-icon" style="left:938px; top:98px;" width="46" height="42" viewBox="0 0 46 42" aria-hidden="true">
    <g fill="none" stroke="var(--navy)" stroke-width="2">
      <line x1="23" y1="3" x2="23" y2="38"/>
      <line x1="5" y1="8" x2="41" y2="8"/>
      <line x1="14" y1="40" x2="32" y2="40"/>
      <path d="M5 8 L1 22 M5 8 L9 22 M41 8 L37 22 M41 8 L45 22"/>
      <path d="M0 22 Q5 28 10 22 Z M36 22 Q41 28 46 22 Z" fill="var(--navy)"/>
    </g>
  </svg>

  <!-- Real Estate Consulting -->
  <svg class="service-icon" style="left:522px; top:142px;" width="52" height="44" viewBox="0 0 52 44" aria-hidden="true">
    <circle cx="18" cy="18" r="14" fill="none" stroke="var(--orange)" stroke-width="4"/>
    <polygon points="18,9 10,17 12,17 12,25 24,25 24,17 26,17" fill="var(--orange)"/>
    <line x1="28" y1="28" x2="44" y2="42" stroke="var(--orange)" stroke-width="6" stroke-linecap="round"/>
  </svg>
  <div class="service service--blue" style="left:576px; top:153px;">Real Estate Consulting</div>

  <!-- Project Management -->
  <div class="service service--orange" style="right:85px; top:195px;">Project Management</div>
  <svg class="service-icon" style="left:942px; top:184px;" width="42" height="42" viewBox="0 0 42 42" aria-hidden="true">
    <rect x="0" y="0" width="42" height="42" rx="6" fill="var(--navy)"/>
    <path d="M11 20 A10 10 0 0 1 29 15" fill="none" stroke="#fff" stroke-width="3"/>
    <polygon points="26,10 33,14 27,19" fill="#fff"/>
    <path d="M31 22 A10 10 0 0 1 13 27" fill="none" stroke="#fff" stroke-width="3"/>
    <polygon points="16,32 9,28 15,23" fill="#fff"/>
  </svg>

  <!-- Market Research -->
  <svg class="service-icon" style="left:520px; top:232px;" width="42" height="42" viewBox="0 0 42 42" aria-hidden="true">
    <g fill="var(--orange)">
      <circle cx="21" cy="6" r="5"/>
      <circle cx="9" cy="16" r="4"/>
      <circle cx="33" cy="16" r="4"/>
      <rect x="15" y="13" width="12" height="28" rx="3"/>
      <rect x="4" y="22" width="10" height="19" rx="3"/>
      <rect x="28" y="22" width="10" height="19" rx="3"/>
    </g>
  </svg>
  <div class="service service--blue" style="left:576px; top:238px;">Market Research</div>

  <!-- Property Development -->
  <div class="service service--orange" style="right:85px; top:280px;">Property Development</div>
  <svg class="service-icon" style="left:937px; top:266px;" width="52" height="36" viewBox="0 0 52 36" aria-hidden="true">
    <g fill="var(--navy)">
      <rect x="0" y="20" width="9" height="16" rx="2"/>
      <rect x="13" y="14" width="9" height="22" rx="2"/>
      <rect x="26" y="6" width="9" height="30" rx="2"/>
      <rect x="39" y="0" width="9" height="36" rx="2"/>
    </g>
  </svg>
</section>

</body>
</html>
```